Magnetic Business card Design do a service provider

Hi,

The company aim is to provide all service needs under one roof. However, at the moment there is only Accounting, Electrical and IT branches. There will be more services coming onboard in the future.

I already have a logo designed (Company name is already part of the logo), I now need a magnetic business card designed.

The business card will contain the following:

- Company Logo
- Contact#
- E-mail
- enough space to add website URL (for future)
Updates

Project Deadline Extended Reason: HI All,The deadline has been extended due to not having enough time to review an overwhelming number of designs that has been submitted by lots of designers.I will be uploading a draft of designs that i have in mind.Thanks. Added Friday, January 22, 2016

Target Market(s)

Residential, Home-based Businesses, Small and Medium businesses

Industry/Entity Type

Business

Contact Information for Business Card

Contact#: 0491 738 552
E-mail: service@brightharborgroup.net.au

Font styles to use
Decorative
Script

Requirements
Must have
• Round edges
• Some form of logo incorporation as a background

```html
<!DOCTYPE html>
<html lang="en">
<head>
<meta charset="utf-8">
<title>Bright Harbor Group – Business Card</title>
<link rel="stylesheet" href="https://fonts.googleapis.com/css2?family=Lato:wght@400;700&display=swap">
<style>
  :root {
    --backdrop: #e4e1de;
    --card-face: #f4f4f3;
    --card-edge: #dcdcdc;
    --band-blue: #0d5499;
    --mark-grey: #c9ccd0;
    --text-light: #ffffff;
  }
  * { margin: 0; padding: 0; box-sizing: border-box; }
  html, body {
    width: 1200px;
    height: 900px;
    overflow: hidden;
    background: var(--backdrop);
  }
  .canvas {
    position: relative;
    width: 1200px;
    height: 900px;
  }
  .card {
    position: absolute;
    left: 150px;
    top: 170px;
    width: 900px;
    height: 560px;
    background: var(--card-face);
    border: 1px solid var(--card-edge);
    border-radius: 26px;
    overflow: hidden;
    box-shadow: 0 10px 30px rgba(0,0,0,0.08);
  }
  .brand-dot {
    position: absolute;
    left: 125px;
    top: 60px;
    width: 170px;
    height: 170px;
    border-radius: 50%;
    background: var(--mark-grey);
  }
  .info-band {
    position: absolute;
    left: 0;
    top: 252px;
    width: 100%;
    height: 246px;
    background: var(--band-blue);
    color: var(--text-light);
    font-family: "Lato", sans-serif;
  }
  .company-name {
    position: absolute;
    left: 52px;
    top: 14px;
    font-size: 46px;
    font-weight: 700;
    letter-spacing: 0.5px;
  }
  .contact-list {
    position: absolute;
    right: 42px;
    top: 116px;
    list-style: none;
    text-align: right;
    font-size: 22px;
    font-weight: 400;
  }
  .contact-item {
    display: flex;
    justify-content: flex-end;
    align-items: center;
    gap: 12px;
    height: 37px;
  }
  .contact-icon {
    width: 18px;
    height: 18px;
    flex: none;
  }
</style>
</head>
<body>
  <main class="canvas">
    <section class="card">
      <div class="brand-dot"></div>
      <div class="info-band">
        <h1 class="company-name">Bright Harbor Group</h1>
        <ul class="contact-list">
          <li class="contact-item">
            <span>0491 738 552</span>
            <svg class="contact-icon" viewBox="0 0 24 24" aria-hidden="true">
              <path fill="#fff" d="M6.6 10.8c1.4 2.8 3.8 5.1 6.6 6.6l2.2-2.2c.3-.3.7-.4 1-.2 1.1.4 2.3.6 3.6.6.6 0 1 .4 1 1V20c0 .6-.4 1-1 1C10.6 21 3 13.4 3 4c0-.6.4-1 1-1h3.5c.6 0 1 .4 1 1 0 1.3.2 2.5.6 3.6.1.3 0 .7-.2 1z"/>
            </svg>
          </li>
          <li class="contact-item">
            <span>service@brightharborgroup.net.au</span>
            <svg class="contact-icon" viewBox="0 0 24 24" aria-hidden="true">
              <rect x="2" y="5" width="20" height="14" fill="#fff"/>
              <path d="M2.5 5.5 12 13l9.5-7.5" fill="none" stroke="#0d5499" stroke-width="1.6"/>
            </svg>
          </li>
          <li class="contact-item">
            <span>www.brightharborgroup.net.au</span>
            <svg class="contact-icon" viewBox="0 0 24 24" aria-hidden="true">
              <g fill="none" stroke="#fff" stroke-width="1.8">
                <circle cx="12" cy="12" r="9.5"/>
                <ellipse cx="12" cy="12" rx="4" ry="9.5"/>
                <path d="M2.5 12h19M4 7h16M4 17h16"/>
              </g>
            </svg>
          </li>
        </ul>
      </div>
    </section>
  </main>
</body>
</html>
```